Zielgruppe
Friseurin für Damen und Herren
Aufgabenstellung
https://lumiraschnitt.de
Bitte erstelle mir anhand der Daten von der Website einen angepassten Entwurf mit Neueröffnung und geben keine Preise an sondern die kunden sollen sich direkt eingeladen führen um persönlich vor Ort vorbei zuschauen.

```html
<!DOCTYPE html>
<html lang="de">
<head>
<meta charset="utf-8">
<title>Lumira Schnitt – Neueröffnung Flyer</title>
<link rel="stylesheet" href="https://fonts.googleapis.com/css2?family=Open+Sans:wght@300;400;600;700&family=Jost:wght@400;500;600&display=swap">
<style>
  :root {
    --sage: #6b7a5c;
    --blush: #e8b4a0;
    --paper: #ffffff;
    --ink: #2a2a2a;
    --red: #d7141c;
    --stage: #f1e2dc;
  }
  * { box-sizing: border-box; margin: 0; padding: 0; }
  html, body { width: 882px; height: 1200px; overflow: hidden; background: var(--stage); }
  body { font-family: "Open Sans", sans-serif; color: var(--ink); position: relative; }

  .sheet-slot { position: absolute; top: 308px; width: 417px; height: 584px; overflow: hidden; }
  .sheet-slot.front-slot { left: 16px; }
  .sheet-slot.back-slot { left: 449px; }

  .page {
    position: absolute; left: 0; top: 0; width: 601px; height: 842px;
    background: var(--paper); overflow: hidden;
    transform: scale(0.6939); transform-origin: 0 0;
  }

  /* ---------- shared ---------- */
  .footer-brand { position: absolute; left: 52px; top: 776px; color: var(--sage); }
  .footer-brand .name { font-size: 19px; letter-spacing: 2px; line-height: 1; }
  .footer-brand .tag { font-family: "Jost", sans-serif; font-size: 10px; letter-spacing: .4px; margin-top: 3px; }
  .footer-address {
    position: absolute; right: 52px; top: 800px;
    font-family: "Jost", sans-serif; font-weight: 600; font-size: 10px; letter-spacing: .8px; color: var(--sage);
  }
  .section-title { font-weight: 400; font-size: 24px; line-height: 1.12; }

  /* ---------- front ---------- */
  .hero-photo {
    position: absolute; left: 0; top: 0; width: 601px; height: 318px;
    background: linear-gradient(135deg, #2b2a2e 0%, #4a3f3c 35%, #7a5a48 55%, #3a3538 80%, #8d8a88 100%);
  }
  .brand-panel {
    position: absolute; left: 262px; top: 166px; width: 300px; height: 152px;
    background: var(--sage);
    display: flex; align-items: center; justify-content: center; gap: 10px;
  }
  .brand-panel .mark { width: 12px; height: 12px; background: var(--paper); }
  .brand-panel .name { font-weight: 300; font-size: 30px; color: var(--paper); }

  .intro-band { position: absolute; left: 0; top: 318px; width: 601px; height: 254px; background: var(--blush); }
  .intro { position: absolute; left: 52px; top: 336px; width: 305px; }
  .intro .section-title { margin-bottom: 18px; }
  .intro p { font-size: 13px; line-height: 1.18; margin-bottom: 15px; }

  .services {
    position: absolute; left: 372px; top: 306px; width: 169px; height: 288px;
    background: var(--paper); border-radius: 18px;
    text-align: center; padding-top: 18px; color: var(--sage);
  }
  .services .kicker { font-family: "Jost", sans-serif; font-size: 15px; line-height: 1; }
  .services .title { font-family: "Jost", sans-serif; font-size: 15px; font-weight: 600; letter-spacing: .8px; margin-bottom: 18px; }
  .services h3 { font-family: "Jost", sans-serif; font-size: 11px; font-weight: 600; letter-spacing: .8px; margin-bottom: 3px; }
  .services p { font-size: 9px; line-height: 1.15; padding: 0 14px; margin-bottom: 18px; }

  .atmosphere {
    position: absolute; left: 214px; top: 572px; width: 387px; height: 207px;
    background: var(--sage); border-radius: 0 0 0 44px; color: var(--paper);
    padding: 40px 30px 0 46px;
  }
  .atmosphere .section-title { margin-bottom: 16px; }
  .atmosphere p { font-size: 12.5px; line-height: 1.2; }

  .opening-badge {
    position: absolute; left: 62px; top: 548px; width: 176px; height: 176px;
    border-radius: 50%; background: var(--red); color: var(--paper);
    display: flex; flex-direction: column; align-items: center; justify-content: center;
    transform: rotate(-22deg); text-align: center;
  }
  .opening-badge .small { font-family: "Jost", sans-serif; font-weight: 600; font-size: 9.5px; line-height: 1.25; }
  .opening-badge .big { font-size: 20px; margin: 10px 0; }
  .opening-badge .addr { font-family: "Jost", sans-serif; font-size: 9.5px; line-height: 1.25; }

  /* ---------- back ---------- */
  .gallery-band { position: absolute; left: 0; top: 0; width: 601px; height: 347px; background: var(--sage); }
  .photo { position: absolute; border-radius: 16px; }
  .photo-curls { left: 54px; top: 48px; width: 296px; height: 263px; background: linear-gradient(135deg, #e9e2dc 0%, #c98a5a 45%, #b46a3c 70%, #e6d3c2 100%); }
  .photo-bottles { left: 361px; top: 47px; width: 189px; height: 126px; background: linear-gradient(135deg, #5a3f2c 0%, #c79a62 50%, #6e4b32 100%); }
  .photo-sprays { left: 361px; top: 186px; width: 189px; height: 125px; background: linear-gradient(135deg, #6a4a32 0%, #7d7f86 50%, #4c3a2e 100%); }

  .contact-band { position: absolute; left: 0; top: 347px; width: 601px; height: 259px; background: var(--blush); }
  .contact { position: absolute; left: 63px; top: 370px; width: 320px; }
  .contact .section-title { margin-bottom: 16px; }
  .contact-grid { display: grid; grid-template-columns: 140px 150px; row-gap: 12px; }
  .contact-grid .label { font-weight: 700; font-size: 9px; letter-spacing: .3px; }
  .contact-grid .value { font-size: 12px; line-height: 1.2; }
  .photo-portrait { left: 405px; top: 366px; width: 145px; height: 215px; border-radius: 12px; background: linear-gradient(160deg, #6e5444 0%, #c9a58c 45%, #3a3a3a 100%); }

  .side-brand {
    position: absolute; left: 50px; top: 670px; width: 150px;
    display: flex; align-items: center; gap: 7px; color: var(--sage);
  }
  .side-brand .mark { width: 8px; height: 8px; background: var(--sage); }
  .side-brand .name { font-weight: 300; font-size: 17px; }

  .philosophy {
    position: absolute; left: 218px; top: 606px; width: 383px; height: 162px;
    background: var(--sage); border-radius: 0 0 0 44px; color: var(--paper);
    padding: 22px 30px 0 46px;
  }
  .philosophy .section-title { margin-bottom: 12px; }
  .philosophy p { font-size: 12.5px; line-height: 1.2; }
</style>
</head>
<body>

<div class="sheet-slot front-slot">
  <main class="page front">
    <div class="hero-photo" role="img" aria-label="Foto: Friseurin färbt im Salon das Haar einer Kundin, Spiegel mit Lichtern im Hintergrund"></div>
    <div class="brand-panel"><span class="mark"></span><span class="name">Lumira Schnitt</span></div>

    <div class="intro-band"></div>
    <section class="intro">
      <h1 class="section-title">Ihr neuer Look wartet</h1>
      <p>In unserem modernen Salon in Lindenau erwarten Sie hochwertige Ausstattung und eine entspannte Atmosphäre. Unser erfahrenes Team sorgt dafür, dass Sie sich rundum wohlfühlen.</p>
      <p>Von klassischen Haarschnitten bis hin zu modernen Colorationen und Extensions - wir bieten Ihnen das komplette Spektrum der Friseurkunst auf höchstem Niveau.</p>
    </section>

    <aside class="services">
      <div class="kicker">UNSERE</div>
      <div class="title">LEISTUNGEN</div>
      <h3>DAMEN</h3>
      <p>Waschen, Schneiden, Föhnen, Styling, Pony, Umformung, Extensions, Strähnen, Färben Balyage, Augenbrauen, Wimpern, Hochstecken, Make-Up, Braut Paket</p>
      <h3>HERREN</h3>
      <p>Waschen, Schneiden, Föhnen, Maschinenschnitt, Haarwasser, Bart schneiden, Rasieren</p>
      <h3>JUNGEN &amp; MÄDCHEN</h3>
    </aside>

    <section class="atmosphere">
      <h2 class="section-title">Moderne Ausstattung &amp;<br>Wohlfühlatmosphäre</h2>
      <p>Lassen Sie sich von unserem Können begeistern. Ob frischer Schnitt, brillante Farbe oder ein verwöhnendes Treatment – wir kreieren den Stil, der Ihre Persönlichkeit perfekt unterstreicht.</p>
    </section>

    <div class="opening-badge">
      <div class="small">LUMIRA SCHNITT &amp;<br>BEAUTYLOUNGE</div>
      <div class="big">NEUERÖFFNUNG!</div>
      <div class="addr">BIRKENWEG 7<br>86852 LINDENAU</div>
    </div>

    <div class="footer-brand"><div class="name">LUMIRA</div><div class="tag">SCHNITT &amp; BEAUTYLOUNGE</div></div>
    <div class="footer-address">BIRKENWEG 7 – 86852 LINDENAU</div>
  </main>
</div>

<div class="sheet-slot back-slot">
  <main class="page back">
    <div class="gallery-band"></div>
    <div class="photo photo-curls" role="img" aria-label="Foto: lange rotblonde Locken werden mit dem Lockenstab gestylt"></div>
    <div class="photo photo-bottles" role="img" aria-label="Foto: Pflegeprodukte in goldenen Flaschen im Regal"></div>
    <div class="photo photo-sprays" role="img" aria-label="Foto: Stylingsprays im Salonregal"></div>

    <div class="contact-band"></div>
    <section class="contact">
      <h2 class="section-title">Wie Sie uns<br>erreichen können</h2>
      <div class="contact-grid">
        <div><div class="label">MONTAG &amp; SONNTAG</div><div class="value">Geschlossen</div></div>
        <div><div class="label">DIENSTAG–DONNERSTAG</div><div class="value">09:00 - 18:00</div></div>
        <div><div class="label">FREITAG</div><div class="value">09:00 - 20:00</div></div>
        <div><div class="label">SAMSTAG</div><div class="value">09:00 - 14:00</div></div>
        <div class="value">Birkenweg 7<br>86852 Lindenau</div>
        <div class="value">08231 47 58 20<br>0152 318 44 76</div>
      </div>
    </section>
    <div class="photo photo-portrait" role="img" aria-label="Foto: Porträt der Inhaberin im Salon"></div>

    <div class="side-brand"><span class="mark"></span><span class="name">Lumira Schnitt</span></div>

    <section class="philosophy">
      <h2 class="section-title">Unsere Philosophie</h2>
      <p>Mehr als nur Haare. Wir schaffen Momente der Schönheit und des Wohlgefühls, die Ihre Persönlichkeit strahlen lassen – mit Herz, Hand und Leidenschaft</p>
    </section>

    <div class="footer-brand"><div class="name">LUMIRA</div><div class="tag">SCHNITT &amp; BEAUTYLOUNGE</div></div>
    <div class="footer-address">BIRKENWEG 7 – 86852 LINDENAU</div>
  </main>
</div>

</body>
</html>
```